PELDRAX Business Cards

We require a business card for our company that provides IT consulting services. We already have a logo that needs to be used on the card. We want a clean professional looking design that incorporates our colours. Our main focus is providing managed services to business, which involves us looking after all of their IT requirements including managing servers/networks, projects, and procurement.

Industry/Entity Type

Information Technology

Requirements
Must have
• our logo, contact information, name, title, phone numbers

```html
<!DOCTYPE html>
<html lang="en">
<head>
<meta charset="utf-8">
<title>PELDRAX Business Cards</title>
<link rel="stylesheet" href="https://fonts.googleapis.com/css2?family=Source+Sans+3:wght@400;600;700&display=swap">
<style>
  :root {
    --backdrop: #3a322e;
    --card: #141414;
    --card-edge: #1e1e1e;
    --brand-blue: #1a9ad6;
    --text-light: #e6e6e6;
    --silver: #d9d9d9;
    --rule: #4a4a4a;
    --dot: #5c6f86;
  }
  * { margin: 0; padding: 0; box-sizing: border-box; }
  html, body {
    width: 1200px; height: 844px; overflow: hidden;
    background: var(--backdrop);
    font-family: "Source Sans 3", "Myriad Pro", Arial, sans-serif;
  }
  .stage { position: relative; width: 1200px; height: 844px; }
  .card {
    position: absolute;
    width: 530px; height: 304px;
    background: var(--card);
    border: 1px solid var(--card-edge);
    box-shadow: 0 8px 24px rgba(0,0,0,0.45);
  }
  /* Back side: contact details */
  .card-back { left: 45px; top: 270px; }
  .card-back .brand-mark {
    position: absolute; left: 0; top: 0; width: 230px; height: 100%;
    display: flex; align-items: center; justify-content: center;
    color: var(--brand-blue); font-weight: 700; font-size: 34px; letter-spacing: 2px;
  }
  .card-back .divider {
    position: absolute; left: 236px; top: 60px; width: 1px; height: 184px;
    background: var(--rule);
  }
  .contact { position: absolute; left: 262px; top: 72px; color: var(--text-light); }
  .contact .person-name {
    color: var(--brand-blue); font-weight: 700; font-size: 21px; letter-spacing: 0.5px;
    text-transform: uppercase; line-height: 1.1;
  }
  .contact .person-title { font-size: 15px; margin-bottom: 10px; }
  .contact .line { display: flex; align-items: center; gap: 7px; font-size: 15px; line-height: 1.35; }
  .contact .line svg { width: 11px; height: 11px; fill: var(--brand-blue); flex: none; }
  .contact .address { font-size: 15px; line-height: 1.3; margin-top: 6px; }

  /* Front side: brand */
  .card-front { left: 625px; top: 270px; }
  .card-front .brand-name {
    position: absolute; left: 0; right: 0; top: 92px; text-align: center;
    color: var(--silver); font-weight: 600; font-size: 54px; letter-spacing: 5px;
  }
  .card-front .social-row {
    position: absolute; left: 60px; right: 60px; top: 196px;
    display: flex; align-items: center; gap: 8px;
  }
  .card-front .social-row .rule { flex: 1; height: 1px; background: var(--rule); }
  .card-front .social-row .dot { width: 13px; height: 13px; border-radius: 50%; background: var(--dot); }
</style>
</head>
<body>
<main class="stage">
  <section class="card card-back">
    <div class="brand-mark">PELDRAX</div>
    <div class="divider"></div>
    <div class="contact">
      <p class="person-name">Daniel Ashcombe</p>
      <p class="person-title">President &amp; Technology Consultant</p>
      <p class="line"><svg viewBox="0 0 12 12" aria-hidden="true"><path d="M2 1h3l1 3-2 1a7 7 0 0 0 3 3l1-2 3 1v3a1 1 0 0 1-1 1A10 10 0 0 1 1 2a1 1 0 0 1 1-1z"/></svg>555-010-2468</p>
      <p class="line"><svg viewBox="0 0 12 12" aria-hidden="true"><path d="M0 2h12v8H0z M0 2l6 4 6-4" /></svg>info@peldrax.com</p>
      <p class="line"><svg viewBox="0 0 12 12" aria-hidden="true"><circle cx="6" cy="6" r="6"/></svg>www.peldrax.com</p>
      <p class="address">48 Harbor Lane<br>Box 2917, Elm Ridge, AB</p>
    </div>
  </section>

  <section class="card card-front">
    <div class="brand-name">PELDRAX</div>
    <div class="social-row">
      <span class="rule"></span>
      <span class="dot"></span><span class="dot"></span><span class="dot"></span><span class="dot"></span><span class="dot"></span>
      <span class="rule"></span>
    </div>
  </section>
</main>
</body>
</html>
```